FULLY CUSTOM MAIN BANNER IMAGE FOR MY WEBSITE-REDESIGN CURRENT

SIZE MUST BE: 1800x829

LOOKING FOR A FULLY CUSTOM MAIN BANNER IMAGE TO BE DESIGNED FOR MY NEW WEBSITE HOMEPAGE http://gridplankstudio.com/dh/derek/vtr_final/index.html THE CONTENT THAT YOU SEE ON THE UPLOADED FILE OR HERE http://gridplankstudio.com/dh/derek/vtr_final/index.html YOU CAN SEE MY EXISTING BANNER IMAGE...IS THE SAME CONTENT I WANT ON THE CUSTOM BANNER IMAGE BUT I WANT THE BANNER IMAGE TO USE IMAGES TO PORTRAY WHAT THE CONTENT SAYS. POSSIBLE INTEGRATE AN INFOGRAPHIC DESIGN IN THE BANNER IMAGE. IM OPEN TO ALL IDEAS.

WHEN SOMEONE GOES TO MY WEBSITE, IMMEDIATELY I WANT THEM TO UNDERSTAND WHAT IT IS I DO.

MY BUSINESS PROVIDES OTHER BUSINESSES WITH THE ABILITY TO CREATE PROMOTIONAL GIVEAWAYS AND MARKETING PROMOTIONS USING GIFT VOUCHERS THAT ARE REDEEMABLE FOR FREE VACATIONS, CRUISES, ALL INCLUSIVE RESORT STAYS, TABLETS, SMARTWATCHES, DINING AND RESTAURANT INCENTIVES AND REWARDS AND MORE.

CURRENTLY THE CONTENT ON THE BANNER IMAGE IS THIS:
BOOST SALES & LEADS OVERNIGHT
BY ENTICING YOUR CUSTOMERS WITH FREE VACATION CERTIFICATES & OTHER HIGH PERCEIVED VALUE INCENTIVES

I HAVE ATTACHED A DOCUMENT WITH IMAGE ASSETTS YOU MAY REVIEW AND USE OR GET IDEAS FROM.

THE BOTTOM LINE IS MY SERVICE HELPS BUSINESSES INCREASE LEADS, CONVERSIONS, CTA, SALES, ETC WITHOUT HAVING TO INCREASE THEIR EXISTING AD SPEND. SIMPLY BY ADDING A FREE OFFER TO ALL THEIR EXISTING ADS WILL DRAMATICALLY INCREASE RESPONSE RATES. SO I WANT THIS BANNER TO REFLECT THIS SOMEHOW....MORE CUSTOMERS USING GIVEAWAYS!

Target Market(s)

B2B, SMALL BUSINESS OWNERS, ENTREPRENEURS, SOLOPRENEURS, MARKETING AGENCIES,

Industry/Entity Type

Digital Marketing

Requirements
Must have
• MUST PORTRAY THE RED CONTENT/TEXT USING IMAGES OF MY ASSETTS AND THE PORTRAY MORE CUSTOMERS---MUST BE FULLY CUSTOM

SIZE MUST BE: 1800x829
Nice to have
• USE CONTENT IN CURRENT BANNER IMAGE ALSO MAKE SURE TO USE THE FREE SAMPLE PKG BUTTON TOO.....MUST BE FULLY CUSTOM

SIZE MUST BE: 1800x829
Should not have
• MUST BE FULLY CUSTOM

SIZE MUST BE: 1800x829

```html
<!DOCTYPE html>
<html lang="en">
<head>
<meta charset="utf-8">
<title>Boost Sales &amp; Leads Overnight</title>
<link rel="stylesheet" href="https://fonts.googleapis.com/css2?family=Archivo+Black&family=Bebas+Neue&family=Libre+Baskerville:wght@700&family=Montserrat:wght@600&display=swap">
<style>
  :root {
    --bg-warm: #e9a458;
    --bg-glow: #f0b76c;
    --bg-mid: #d6ab96;
    --bg-cool: #b8a3a2;
    --bg-top-right: #e2dfdf;
    --ink: #2a2522;
    --white: #ffffff;
    --hero-light: #ddd2cc;
    --hero-mid: #c4b3ae;
  }
  html, body {
    margin: 0;
    padding: 0;
    width: 1200px;
    height: 578px;
    overflow: hidden;
  }
  .banner {
    position: relative;
    width: 1200px;
    height: 578px;
    overflow: hidden;
    background:
      radial-gradient(ellipse 420px 300px at 300px 90px, rgba(240,183,108,0.8), rgba(240,183,108,0) 70%),
      radial-gradient(ellipse 520px 260px at 1150px 40px, var(--bg-top-right), rgba(226,223,223,0) 75%),
      linear-gradient(180deg, rgba(184,163,162,0) 55%, var(--bg-cool) 100%),
      linear-gradient(90deg, var(--bg-warm) 0%, var(--bg-glow) 25%, var(--bg-mid) 55%, var(--bg-cool) 100%);
  }
  .hero-visual {
    position: absolute;
    left: 713px;
    top: 32px;
    width: 428px;
    height: 356px;
    background: linear-gradient(180deg, rgba(221,210,204,0.35) 0%, rgba(196,179,174,0.55) 100%);
  }
  .headline {
    position: absolute;
    left: 0;
    top: 0;
  }
  .headline .boost {
    font-family: "Archivo Black", sans-serif;
    fill: var(--white);
  }
  .headline .sales-leads {
    font-family: "Montserrat", sans-serif;
    font-weight: 600;
    fill: var(--ink);
  }
  .headline .ampersand {
    font-family: "Libre Baskerville", serif;
    font-weight: 700;
    fill: var(--ink);
  }
  .headline .overnight-box { fill: var(--ink); }
  .headline .overnight {
    font-family: "Bebas Neue", sans-serif;
    fill: var(--white);
  }
  .headline .subhead {
    font-family: "Bebas Neue", sans-serif;
    fill: var(--ink);
    stroke: var(--ink);
    stroke-width: 0.8;
  }
</style>
</head>
<body>
  <main class="banner">
    <div class="hero-visual" role="img" aria-label="Orange arrow launching upward like a rocket from a billowing cloud of smoke"></div>

    <svg class="headline" width="1200" height="578" viewBox="0 0 1200 578" aria-labelledby="headline-title">
      <title id="headline-title">Boost sales &amp; leads overnight by enticing your customers with free vacation certificates &amp; other high perceived value incentives</title>

      <text class="boost" x="43" y="241" font-size="163" textLength="630" lengthAdjust="spacingAndGlyphs">BOOST</text>

      <text class="sales-leads" x="43" y="287" font-size="44" textLength="151" lengthAdjust="spacingAndGlyphs">SALES</text>
      <text class="sales-leads" x="43" y="333" font-size="44" textLength="151" lengthAdjust="spacingAndGlyphs">LEADS</text>

      <text class="ampersand" x="212" y="337" font-size="114" textLength="77" lengthAdjust="spacingAndGlyphs">&amp;</text>

      <rect class="overnight-box" x="301" y="256" width="369" height="78"/>
      <text class="overnight" x="309" y="328" font-size="90" textLength="354" lengthAdjust="spacing">OVERNIGHT</text>

      <text class="subhead" x="42" y="382" font-size="41" textLength="602" lengthAdjust="spacingAndGlyphs">BY ENTICING YOUR CUSTOMERS WITH FREE VACATION</text>
      <text class="subhead" x="42" y="423" font-size="41" textLength="669" lengthAdjust="spacingAndGlyphs">CERTIFICATES &amp; OTHER HIGH PERCEIVED VALUE INCENTIVES</text>
    </svg>
  </main>
</body>
</html>
```